High Quality Business card for Property Management Agency - Super Classy and professional design

High Quality Business card design.

We need a business card designed for our Property Management Agency.
We are located on Sydney's Northern Beaches and manage beautiful properties along the beach and harbor.
We need a design that oozes modern, classy and professional.
I would like it to be double sided with contact details and logo on the front and just the logo on the back.

I need a print ready PDF version of the file as well as an editable photoshop (PSD) version of the file.

Logo and information details attached.

Target Market(s)

Property owners/investors, Male and Female Aged 28-65

Industry/Entity Type

Real Estate

Contact Information for Business Card

Tom Carrick
Tel: 0467 239 018
Email: tom@harvestlaneestates.com.au
Website: www.harvestlaneestates.com.au
Address: Level 2, 17 Wattlecourt Rd, Dunmarra NSW 2187

Font styles to use
Sans Serif

Requirements
Must have
• - Logo front and back
• - Business card details listed above and attached
• - Colour
Nice to have
• Sleek and professional

```html
<!DOCTYPE html>
<html lang="en">
<head>
<meta charset="utf-8">
<title>Harvest Lane Estates – Business Card</title>
<link rel="stylesheet" href="https://fonts.googleapis.com/css2?family=Montserrat:wght@400;500;600&display=swap">
<style>
  :root {
    --bg: #e9e6e1;
    --card: #ffffff;
    --teal: #17918f;
    --grey: #a3a5a6;
    --ink: #2b2b2b;
    --name: #4a4a4a;
    --body: #555555;
    --knock: #ffffff;
  }
  * { margin: 0; padding: 0; box-sizing: border-box; }
  html, body { width: 1200px; height: 800px; overflow: hidden; }
  body {
    background: var(--bg);
    font-family: "Montserrat", sans-serif;
    position: relative;
  }
  .card {
    position: absolute;
    top: 252px;
    width: 520px;
    height: 297px;
    background: var(--card);
    overflow: hidden;
    box-shadow: 0 6px 18px rgba(0,0,0,0.12);
  }
  .card--logo { left: 60px; }
  .card--details { left: 620px; }

  /* straight accent bands */
  .band { position: absolute; top: 0; bottom: 0; }
  .card--logo .band--teal { left: 0; width: 16px; background: var(--teal); }
  .card--logo .band--grey { left: 22px; width: 4px; background: var(--grey); }
  .card--details .band--teal { right: 0; width: 16px; background: var(--teal); }
  .card--details .band--grey { right: 22px; width: 4px; background: var(--grey); }

  .brand {
    position: absolute;
    inset: 0 0 0 26px;
    display: flex;
    align-items: center;
    justify-content: center;
    gap: 12px;
  }
  .brand__dot {
    width: 20px; height: 20px; border-radius: 50%;
    background: var(--teal);
    flex: none;
  }
  .brand__name {
    font-size: 26px;
    font-weight: 600;
    color: var(--ink);
    letter-spacing: 0.5px;
    text-transform: uppercase;
    line-height: 1;
    white-space: nowrap;
  }

  .contact { position: absolute; left: 36px; top: 58px; }
  .contact__name {
    font-size: 33px;
    font-weight: 500;
    color: var(--name);
    letter-spacing: 1.5px;
    text-transform: uppercase;
    margin-bottom: 20px;
    white-space: nowrap;
  }
  .contact__list { list-style: none; padding-left: 30px; }
  .contact__item {
    display: flex;
    align-items: flex-start;
    gap: 14px;
    font-size: 11.5px;
    line-height: 1.35;
    color: var(--body);
    margin-bottom: 15px;
    white-space: nowrap;
  }
  .contact__icon { width: 16px; height: 16px; flex: none; margin-top: 1px; }
  .contact__icon .solid { fill: var(--ink); }
  .contact__icon .knock { fill: var(--knock); }
  .contact__icon .line { fill: none; stroke: var(--knock); stroke-width: 1.2; }
</style>
</head>
<body>

<section class="card card--logo">
  <span class="band band--teal"></span>
  <span class="band band--grey"></span>
  <div class="brand">
    <span class="brand__dot"></span>
    <span class="brand__name">Harvest Lane Estates</span>
  </div>
</section>

<section class="card card--details">
  <span class="band band--teal"></span>
  <span class="band band--grey"></span>
  <div class="contact">
    <h1 class="contact__name">Tom Carrick</h1>
    <ul class="contact__list">
      <li class="contact__item">
        <svg class="contact__icon" viewBox="0 0 16 16" aria-hidden="true"><path class="solid" d="M8 1 L15 8 H13 V15 H9.5 V10.5 H6.5 V15 H3 V8 H1 Z"/></svg>
        <span>Level 2, 17 Wattlecourt Rd,<br>Dunmarra NSW 2187</span>
      </li>
      <li class="contact__item">
        <svg class="contact__icon" viewBox="0 0 16 16" aria-hidden="true"><circle class="solid" cx="8" cy="8" r="8"/><path class="knock" d="M5.2 4 L6.8 4 L7.4 6 L6.4 6.9 C6.9 8 7.9 9 9 9.6 L9.9 8.6 L11.9 9.2 L11.9 10.8 C11 11.8 9 11.6 7 10 C5 8.4 4.2 6 5.2 4Z"/></svg>
        <span>0467 239 018</span>
      </li>
      <li class="contact__item">
        <svg class="contact__icon" viewBox="0 0 16 16" aria-hidden="true"><circle class="solid" cx="8" cy="8" r="8"/><ellipse class="line" cx="8" cy="8" rx="3" ry="7"/><path class="line" d="M1 8 H15 M2.5 4.5 H13.5 M2.5 11.5 H13.5"/></svg>
        <span>tom@harvestlaneestates.com.au<br>www.harvestlaneestates.com.au</span>
      </li>
    </ul>
  </div>
</section>

</body>
</html>
```